agricultural technology company needs business cards*

design a business card that represents our business well. please see our website: vastrelbyfieldseal.com.au
professional, simple, clean lines, not complicated or floral.....

```html
<!DOCTYPE html>
<html lang="en">
<head>
<meta charset="utf-8">
<title>Vastrel Byfield Seal – Business Cards</title>
<link href="https://fonts.googleapis.com/css2?family=Arimo:wght@400;700&display=swap" rel="stylesheet">
<style>
  :root {
    --backdrop: #2b2b2b;
    --card: #ffffff;
    --green: #00a94f;
    --green-deep: #019a48;
    --lime: #8dc63f;
    --navy: #1b2a4a;
    --ink: #3a3a3a;
    --rule: #d6d6d6;
  }
  * { margin: 0; padding: 0; box-sizing: border-box; }
  html, body { width: 1200px; height: 716px; overflow: hidden; }
  body {
    background: var(--backdrop);
    font-family: "Arimo", Arial, sans-serif;
    position: relative;
  }
  .card {
    position: absolute;
    top: 208px;
    width: 520px;
    height: 300px;
    background: var(--card);
    overflow: hidden;
    box-shadow: 0 6px 18px rgba(0,0,0,.35);
  }
  .card svg.card-shapes { position: absolute; inset: 0; }
  .card--front { left: 60px; }
  .card--back { left: 620px; }

  .front-panel {
    position: absolute;
    left: 95px; top: 0;
    width: 425px; height: 300px;
    background: var(--green);
    border-top-left-radius: 80px;
  }
  .front-swoosh {
    position: absolute;
    left: 95px; top: 0;
    width: 200px; height: 70px;
    background: linear-gradient(160deg, var(--lime), #c8e6a8 55%, var(--green));
  }
  .front-map {
    position: absolute;
    left: 170px; top: 40px;
    width: 320px; height: 160px;
    background: radial-gradient(ellipse at center, rgba(0,120,55,.35), rgba(0,120,55,0) 70%);
  }
  .front-name {
    position: absolute;
    left: 232px; top: 196px;
    color: #fff;
    font-weight: 700;
    font-size: 26px;
    line-height: 25px;
    letter-spacing: -0.5px;
  }
  .front-web {
    position: absolute;
    left: 232px; top: 252px;
    color: #fff;
    font-size: 13px;
  }

  .back-name {
    position: absolute;
    left: 34px; top: 96px;
    color: var(--navy);
    font-weight: 700;
    font-size: 29px;
    line-height: 28px;
    letter-spacing: -0.6px;
  }
  .back-divider {
    position: absolute;
    left: 262px; top: 84px;
    width: 1px; height: 118px;
    background: var(--rule);
  }
  .contact {
    position: absolute;
    left: 280px; top: 84px;
    color: var(--ink);
    font-size: 13px;
    line-height: 16px;
  }
  .contact__person { color: var(--navy); font-weight: 700; font-size: 15px; }
  .contact__role { color: var(--green); font-size: 15px; margin-bottom: 8px; }
  .contact__line { display: flex; align-items: center; gap: 6px; }
  .contact__icon {
    width: 13px; height: 13px;
    display: inline-flex; align-items: center; justify-content: center;
  }
  .contact__icon--phone { background: var(--navy); }
  .contact__icon--mail { background: var(--lime); }
  .contact__address { margin-bottom: 6px; }
</style>
</head>
<body>

  <section class="card card--front" aria-label="Business card front">
    <div class="front-panel"></div>
    <div class="front-swoosh" role="img" aria-label="Curved leaf swoosh in lime and white"></div>
    <div class="front-map" role="img" aria-label="Faint dotted world map in deep green"></div>
    <div class="front-name">Vastrel<br>Byfield Seal</div>
    <div class="front-web">www.vastrelbyfieldseal.com.au</div>
  </section>

  <section class="card card--back" aria-label="Business card back">
    <svg class="card-shapes" width="520" height="300" viewBox="0 0 520 300">
      <path d="M0,268 L200,268 L212,254 L520,254 L520,262 L216,262 L204,276 L0,276 Z" fill="var(--lime)"/>
      <path d="M0,276 L204,276 L216,262 L520,262 L520,300 L0,300 Z" fill="var(--green)"/>
    </svg>
    <div class="back-name">Vastrel<br>Byfield Seal</div>
    <div class="back-divider"></div>
    <div class="contact">
      <div class="contact__person">Daan Verhoef</div>
      <div class="contact__role">Founder &amp; Co-Owner</div>
      <div class="contact__address">12 Harlow Road,<br>Seabrook, WA 6090</div>
      <div class="contact__line">
        <span class="contact__icon contact__icon--phone">
          <svg width="9" height="9" viewBox="0 0 10 10"><path d="M2,1 L4,1 L4.5,3 L3.5,4 Q4.5,6 6,6.5 L7,5.5 L9,6 L9,8 Q5,9 1,5 Q1,2 2,1 Z" fill="#fff"/></svg>
        </span>1300 482 516
      </div>
      <div class="contact__line">
        <span class="contact__icon contact__icon--mail">
          <svg width="9" height="9" viewBox="0 0 10 10"><rect x="1" y="2.5" width="8" height="5" fill="none" stroke="#fff"/><path d="M1,2.5 L5,5.5 L9,2.5" fill="none" stroke="#fff"/></svg>
        </span>info@vastrelbyfieldseal.com.au
      </div>
      <div class="contact__line">www.vastrelbyfieldseal.com.au</div>
    </div>
  </section>

</body>
</html>
```